Martin Hale PA Card Logo

Current logo attached. Its 25 year old logo I have used. Looking for a new fresh elegant professional look/design for a law firm that has high net worth clientele and is estate planning business law firm. Firm mis in Palm Beach Florida.
One sided card linen stock white will be used. Logo section name section. Logo should include nice elegant design using the letter "M" perhapa (I am not wed to current font of the M on current logo.) Be creative there with logo design. My initials are MH.......color scheme I figure 3 tone... Raised Gold Foil, Blue name of firm = Martin Hale, P.A. My practice focus is Family and Business Asset Protection. My name is Martin M. Hale, Esq. Practice specialties include Asset Protection trusts, Business Succession Planning, LLC law, Estate Planning, Medicaid Planning (Maybe put those topics in bullets in a section of card. Bottom of card can be reserved smaller print address phone website and email address. Address section is not as important as logo and topics of practice on front. I foresee address section can be in dark blue. MY name and Topics dark blue as well.
Target Market(s)
affluent; business owners executives; wealth 2-10 million net worth
Industry/Entity Type
business law and estate planning
Contact Information for Business Card
White thick linen one sided

```html
<!DOCTYPE html>
<html lang="en">
<head>
<meta charset="utf-8">
<title>Martin Hale, P.A. – Business Card</title>
<link rel="stylesheet" href="https://fonts.googleapis.com/css2?family=Cinzel:wght@600&family=Arimo:wght@400&display=swap">
<style>
  :root {
    --page-bg: #e9e9e9;
    --card-white: #ffffff;
    --navy: #253951;
    --name-navy: #26395a;
    --gold: #d8c18f;
    --frame-gold: #cdb57d;
    --light-text: #ffffff;
  }
  * { margin: 0; padding: 0; box-sizing: border-box; }
  html, body { width: 1200px; height: 1200px; overflow: hidden; }
  body { background: var(--page-bg); position: relative; font-family: "Arimo", Arial, sans-serif; }

  .card { position: absolute; border-radius: 30px; overflow: hidden; }
  .card-front { left: 241px; top: 155px; width: 729px; height: 412px; background: var(--card-white); }
  .card-back { left: 234px; top: 651px; width: 730px; height: 415px; background: var(--navy); }

  .contact-band { position: absolute; left: 0; top: 182px; width: 100%; height: 230px; background: var(--navy); color: var(--light-text); }

  .brand-frame { position: absolute; border: 2px solid var(--frame-gold); }
  .brand-square { position: absolute; background: var(--gold); }
  .brand-name { position: absolute; font-family: "Cinzel", "Times New Roman", serif; font-weight: 600; white-space: nowrap; line-height: 1; }
  .brand-tagline { position: absolute; font-family: "Cinzel", "Times New Roman", serif; font-weight: 600; white-space: nowrap; line-height: 1; }

  .card-front .brand-frame { left: 113px; top: 55px; width: 511px; height: 91px; }
  .card-front .brand-square { left: 3px; top: 3px; width: 80px; height: 81px; }
  .card-front .brand-name { left: 98px; top: 13px; font-size: 37px; color: var(--name-navy); }
  .card-front .brand-tagline { left: 99px; top: 53px; font-size: 20px; color: var(--name-navy); }

  .card-back .brand-frame { left: 57px; top: 153px; width: 639px; height: 112px; }
  .card-back .brand-square { left: 3px; top: 3px; width: 103px; height: 102px; }
  .card-back .brand-name { left: 122px; top: 18px; font-size: 45px; color: var(--light-text); }
  .card-back .brand-tagline { left: 124px; top: 66px; font-size: 25px; color: var(--light-text); }

  .address { position: absolute; left: 52px; top: 26px; font-size: 15px; line-height: 19px; }
  .contact-list { position: absolute; left: 49px; top: 94px; list-style: none; font-size: 15px; }
  .contact-list li { display: flex; align-items: center; height: 23.5px; }
  .contact-list svg { width: 19px; height: 19px; margin-right: 7px; flex: none; }
</style>
</head>
<body>
  <section class="card card-front">
    <div class="brand-frame">
      <div class="brand-square"></div>
      <div class="brand-name">Martin Hale, P.A.</div>
      <div class="brand-tagline">Elder Law Attorney</div>
    </div>
    <div class="contact-band">
      <p class="address">P.O. Box, Street Name,<br>Countryname , ZIPCODE 0000</p>
      <ul class="contact-list">
        <li>
          <svg viewBox="0 0 20 20" fill="none" stroke="#fff" stroke-width="1.3"><circle cx="10" cy="10" r="8.8"/><path d="M6.5 5.5l2 .2.6 2-1.2 1c.7 1.4 1.6 2.3 3 3l1-1.2 2 .6.2 2c-4 .8-8.2-3.4-7.6-7.6z" fill="#fff" stroke="none"/></svg>
          561 555 0142
        </li>
        <li>
          <svg viewBox="0 0 20 20" fill="none" stroke="#fff" stroke-width="1.3"><circle cx="10" cy="10" r="8.8"/><rect x="7" y="5" width="6" height="10" rx="1"/></svg>
          561 555 0187
        </li>
        <li>
          <svg viewBox="0 0 20 20" fill="none" stroke="#fff" stroke-width="1.3"><circle cx="10" cy="10" r="8.8" fill="#fff"/><rect x="5.5" y="7" width="9" height="6.5" fill="#253951" stroke="none"/><path d="M5.5 7l4.5 3.5L14.5 7" stroke="#fff" stroke-width="1"/></svg>
          info@martinhalelaw.com
        </li>
        <li>
          <svg viewBox="0 0 20 20" fill="none" stroke="#fff" stroke-width="1.1"><circle cx="10" cy="10" r="8.8"/><circle cx="10" cy="10" r="5"/><ellipse cx="10" cy="10" rx="2.2" ry="5"/><path d="M5 10h10"/></svg>
          www.martinhalelaw.com
        </li>
      </ul>
    </div>
  </section>

  <section class="card card-back">
    <div class="brand-frame">
      <div class="brand-square"></div>
      <div class="brand-name">Martin Hale, P.A.</div>
      <div class="brand-tagline">Elder Law Attorney</div>
    </div>
  </section>
</body>
</html>
```